RV Park - Advertising RV Park using Billboard 12 ft wide by 6 ft tall size

We need a sign for a relatively new RV Park called Bramblewood of Carver RV Park at 2745 Danbury Road, Murphy , NC. The sign should include our web address and phone number. bramblewoodcarverrv.example, 555-314-2967. We would like to see designs that include nice color and no tacky cartoons. Final design should communicate a nice and safe RV Park. We would also like to include quick directions - Just Ahead! Left on Kestrel Rd then left on Danbury Rd. (A nice motor home or RV representation may be nice but not mandatory to be included.) Classic but eye catching design. Sign is 12 ft wide by 6 ft tall in size. Will likely be vinyl printed.

```html
<!DOCTYPE html>
<html lang="en">
<head>
<meta charset="utf-8">
<title>Bramblewood of Carver RV Park – Billboard</title>
<link href="https://fonts.googleapis.com/css2?family=Roboto+Slab:wght@500;700;800&display=swap" rel="stylesheet">
<style>
  :root {
    --page-bg: #e4e4e4;
    --panel: #ffffff;
    --maroon: #6b1414;
    --ink: #1d1d1d;
    --white: #ffffff;
  }
  html, body {
    margin: 0;
    width: 1052px;
    height: 1200px;
    overflow: hidden;
    background: var(--page-bg);
  }
  .billboard {
    position: absolute;
    left: 26px;
    top: 350px;
    width: 1000px;
    height: 500px;
    background: var(--panel);
    box-shadow: 0 6px 18px rgba(0,0,0,0.25);
    overflow: hidden;
    font-family: "Roboto Slab", serif;
  }
  .billboard-art {
    position: absolute;
    inset: 0;
  }
  .brand-name {
    position: absolute;
    left: 42px;
    top: 40px;
    width: 230px;
    margin: 0;
    text-align: center;
    color: var(--maroon);
    font-weight: 700;
    font-size: 34px;
    line-height: 1.1;
  }
  .headline {
    position: absolute;
    left: 42px;
    top: 186px;
    margin: 0;
    color: var(--maroon);
    font-weight: 800;
    font-size: 50px;
    line-height: 1;
  }
  .directions {
    position: absolute;
    left: 42px;
    top: 252px;
    margin: 0;
    color: var(--ink);
    font-weight: 500;
    font-size: 23px;
    line-height: 32px;
  }
  .contact {
    position: absolute;
    left: 38px;
    top: 355px;
    margin: 0;
    padding: 0;
    list-style: none;
    color: var(--white);
  }
  .contact-item {
    display: flex;
    align-items: center;
    gap: 16px;
    font-weight: 700;
  }
  .contact-phone { font-size: 44px; height: 64px; }
  .contact-web { font-size: 25px; height: 50px; }
  .contact-icon { flex: none; }
</style>
</head>
<body>
  <section class="billboard">
    <svg class="billboard-art" width="1000" height="500" viewBox="0 0 1000 500">
      <defs>
        <linearGradient id="scene-tones" x1="0" y1="0" x2="0" y2="1">
          <stop offset="0" stop-color="#9fb0c2"/>
          <stop offset="0.3" stop-color="#c9d3dd"/>
          <stop offset="0.5" stop-color="#5f7d63"/>
          <stop offset="0.72" stop-color="#4f8a4a"/>
          <stop offset="1" stop-color="#6f9a35"/>
        </linearGradient>
      </defs>
      <rect class="contact-band" x="0" y="345" width="720" height="135" fill="var(--maroon)"/>
      <path class="photo-edge" d="M482,0 Q668,250 434,500" fill="none" stroke="var(--maroon)" stroke-width="14"/>
      <path class="scene-photo" role="img" aria-label="Photo of a white travel trailer parked on a grassy hillside beside a lake with misty green mountains"
            d="M490,0 Q676,250 442,500 L1000,500 L1000,0 Z" fill="url(#scene-tones)"/>
    </svg>

    <h1 class="brand-name">Bramblewood of Carver</h1>

    <h2 class="headline">Just Ahead!</h2>
    <p class="directions">Left on Kestrel Rd then<br>left on Danbury Rd</p>

    <ul class="contact">
      <li class="contact-item contact-phone">
        <svg class="contact-icon" width="28" height="28" viewBox="0 0 28 28" aria-hidden="true">
          <circle cx="14" cy="14" r="14" fill="var(--white)"/>
          <path d="M10 7.5c.6-.4 1.3-.2 1.6.4l1.2 2.4c.3.6.1 1.2-.4 1.6l-.9.6c.6 1.6 1.8 2.9 3.4 3.6l.7-.9c.4-.5 1.1-.6 1.6-.3l2.3 1.3c.6.3.8 1 .4 1.6l-.9 1.4c-.5.7-1.4 1-2.2.8-4.2-1.2-7.3-4.4-8.4-8.6-.2-.8.1-1.7.8-2.2z" fill="var(--maroon)"/>
        </svg>
        555-314-2967
      </li>
      <li class="contact-item contact-web">
        <svg class="contact-icon" width="28" height="28" viewBox="0 0 28 28" aria-hidden="true">
          <circle cx="14" cy="14" r="14" fill="var(--white)"/>
          <g fill="none" stroke="var(--maroon)" stroke-width="1.6">
            <circle cx="14" cy="14" r="8"/>
            <ellipse cx="14" cy="14" rx="3.5" ry="8"/>
            <line x1="6" y1="14" x2="22" y2="14"/>
          </g>
        </svg>
        bramblewoodcarverrv.example
      </li>
    </ul>
  </section>
</body>
</html>
```